KO Mall

I need a powerful power point presentation to translate my executive summary into words and graphics, utilizing all the resources necessary to produce a 12-14 page Powerpoint pitch book in order to convince potential investors of my business idea. The concept behind the Mall is to develop a number of unique standalone community malls, targeting the under-served residential communities in -.
The Mall will be built around family and their younger generation audience, creating a unique atmosphere that is conducive to making the MALL a regular local destination for the residents.
Each community mall will be remarkably designed around light, nature and music in a way not done before. The Mall will bring essential goods and services to each community that has been neglected by the large mall operators. [PLEASE CHECK ATTACHMENT OF THE PITCH BOOK WHICH I DREW OUT TO GIVE YOU AN IDEA OF THE ESSENTIAL PAGES]
Updates

I have added the LOGO of the project to give you an idea of how to choose your color schemes for the powerpoint presentation.

Reason: Interesting submissions. Need more time to assess with designers..

Dear all,

I am on the verge of finalizing with a designer. Anyone who has or about to start working on a design, I would ask you not to in order not to waste your time. Many thanks for your interests..

Target Market(s)

Mid to upper market. Colours should be greys, blacks, browns and earthy.. This is a mall project in the middle of the desert.

Industry/Entity Type

Residential

Requirements
Must have
• Since this is a real estate project, there must be maps of the area surrounding the project, the actual location using google maps, nice soft rounded/friendly graphics showing returns to investors and cost of project, snap shots of mall designs that give an idea of the design (actual designs will be given later)... Etc..
Nice to have
• Cool graphics, info graphics explaining things in a way investors can grab, especially relating to financial matters. Ha to have a good sense of continuity in the presentation..
Should not have
• too bright or fun colours... This is a serious real estate project BUT it is designed for the younger generation but for the enjoyment of all. The only bright colours will come from the logo which is under design. The logo will have an element of orange and red in it.

```html
<!DOCTYPE html>
<html lang="en">
<head>
<meta charset="utf-8">
<title>KO Mall – Pitch Book Slides</title>
<link href="https://fonts.googleapis.com/css2?family=Carlito:wght@400;700&display=swap" rel="stylesheet">
<style>
  :root {
    --stage: #000000;
    --slide: #ffffff;
    --ink: #1a1a1a;
    --grey-dark: #5a5a5a;
    --grey-mid: #808080;
    --grey-light: #b3b3b3;
    --grey-pale: #e4e4e4;
    --brand-grey: #6b6b6b;
    --brand-orange: #e8731c;
    --step-1: #c0392e;
    --step-2: #c4622f;
    --step-3: #bf8f30;
    --step-4: #afbd31;
    --step-5: #7fb23d;
  }
  * { box-sizing: border-box; margin: 0; padding: 0; }
  html, body { width: 1200px; height: 960px; overflow: hidden; background: var(--stage); }
  body { position: relative; font-family: "Carlito", "Calibri", sans-serif; color: var(--ink); }

  .slide {
    position: absolute; width: 553px; height: 413px;
    background: var(--slide); overflow: hidden;
  }
  .slide--cover { left: 34px; top: 45px; }
  .slide--timeline { left: 613px; top: 45px; }
  .slide--rationale { left: 34px; top: 489px; }
  .slide--chart { left: 613px; top: 489px; }

  .header-bar {
    position: absolute; left: 0; top: 0; width: 100%; height: 19px;
    background: linear-gradient(#f4f4f4, #cdcdcd);
    font-size: 12px; line-height: 19px; padding-left: 42px; color: var(--ink);
  }

  .footer-wave { position: absolute; left: 0; bottom: 0; width: 553px; height: 80px; }
  .footer-badge {
    position: absolute; left: 22px; bottom: 6px; width: 60px; height: 60px;
    border-radius: 50%; background: var(--slide);
    border: 4px solid #d6d6d6; box-shadow: 0 1px 3px rgba(0,0,0,.2);
    display: flex; align-items: center; justify-content: center;
    font-size: 15px; font-weight: 700; color: var(--brand-orange);
  }

  .slide-title {
    position: absolute; left: 0; width: 100%; text-align: center;
    font-size: 26px; font-weight: 400; color: var(--ink);
  }

  /* cover */
  .cover-name {
    position: absolute; left: 0; top: 120px; width: 100%; text-align: center;
    font-size: 64px; font-weight: 400; color: var(--brand-grey);
  }
  .cover-rule {
    position: absolute; left: 137px; top: 251px; width: 266px;
    border-top: 4px dotted var(--brand-orange);
  }

  /* timeline */
  .timeline { position: absolute; left: 19px; top: 100px; width: 516px; height: 44px; }
  .timeline-notes { position: absolute; left: 11px; top: 149px; display: flex; }
  .timeline-note {
    width: 102px; font-size: 13.5px; line-height: 16px; padding-left: 11px; position: relative;
  }
  .timeline-note::before { content: "•"; position: absolute; left: 2px; }

  /* rationale */
  .section-tag { position: absolute; right: 9px; top: 24px; font-size: 12px; }
  .pillar-list { position: absolute; left: 23px; top: 71px; list-style: none; }
  .pillar { position: relative; width: 500px; height: 50px; margin-bottom: 5px; }
  .pillar-track {
    position: absolute; left: 170px; top: 3px; width: 330px; height: 44px;
    border-radius: 5px; border: 2px solid #f2f2f2;
    box-shadow: inset 0 0 0 1px rgba(255,255,255,.6);
  }
  .pillar-label {
    position: absolute; left: 0; top: 0; width: 179px; height: 50px; border-radius: 5px;
    color: #fff; font-size: 15px; line-height: 24px; text-align: center; padding-top: 1px;
    box-shadow: 0 2px 3px rgba(0,0,0,.35);
  }
  .pillar:nth-child(1) .pillar-label { background: linear-gradient(#dc5a4d, var(--step-1)); }
  .pillar:nth-child(1) .pillar-track { background: #e7cdcd; }
  .pillar:nth-child(2) .pillar-label { background: linear-gradient(#dc7c48, var(--step-2)); }
  .pillar:nth-child(2) .pillar-track { background: #e8d7cf; }
  .pillar:nth-child(3) .pillar-label { background: linear-gradient(#d6a94b, var(--step-3)); }
  .pillar:nth-child(3) .pillar-track { background: #e8e0d1; }
  .pillar:nth-child(4) .pillar-label { background: linear-gradient(#ced550, var(--step-4)); }
  .pillar:nth-child(4) .pillar-track { background: #e3e6d4; }
  .pillar:nth-child(5) .pillar-label { background: linear-gradient(#a0cc58, var(--step-5)); }
  .pillar:nth-child(5) .pillar-track { background: #dde6d4; }

  /* chart */
  .bar-chart { position: absolute; left: 0; top: 0; width: 553px; height: 330px; font-family: "Carlito", "Calibri", sans-serif; }
</style>
</head>
<body>

<section class="slide slide--cover">
  <div class="cover-name">KO Mall</div>
  <div class="cover-rule"></div>
  <svg class="footer-wave" viewBox="0 0 553 80" aria-hidden="true">
    <defs>
      <linearGradient id="waveFill1" x1="0" y1="0" x2="0" y2="1">
        <stop offset="0" stop-color="#f3f3f3"/><stop offset="1" stop-color="#dcdcdc"/>
      </linearGradient>
    </defs>
    <path d="M0 2 C40 40 140 52 260 44 C380 36 470 22 553 24 L553 80 L0 80 Z" fill="url(#waveFill1)"/>
    <path d="M0 2 C40 40 140 52 260 44 C380 36 470 22 553 24" fill="none" stroke="#c8c8c8" stroke-width="1.5"/>
    <path d="M70 60 C200 66 380 42 553 40" fill="none" stroke="#bdbdbd" stroke-width="3"/>
  </svg>
  <div class="footer-badge">KO</div>
</section>

<section class="slide slide--timeline">
  <div class="header-bar">KO Mall</div>
  <h1 class="slide-title" style="top:34px;">Development Timeline</h1>
  <svg class="timeline" viewBox="0 0 516 44">
    <defs>
      <linearGradient id="gloss" x1="0" y1="0" x2="0" y2="1">
        <stop offset="0" stop-color="#fff" stop-opacity=".35"/>
        <stop offset=".5" stop-color="#fff" stop-opacity=".08"/>
        <stop offset="1" stop-color="#000" stop-opacity=".08"/>
      </linearGradient>
    </defs>
    <g font-family="Carlito, Calibri, sans-serif" font-size="14" fill="#fff" text-anchor="middle">
      <polygon points="0,2 92,2 104,22 92,42 0,42 10,22" fill="var(--step-1)"/>
      <polygon points="0,2 92,2 104,22 92,42 0,42 10,22" fill="url(#gloss)"/>
      <text x="54" y="27">2009</text>
      <polygon points="103,2 195,2 207,22 195,42 103,42 113,22" fill="var(--step-2)"/>
      <polygon points="103,2 195,2 207,22 195,42 103,42 113,22" fill="url(#gloss)"/>
      <text x="157" y="27">2010</text>
      <polygon points="206,2 298,2 310,22 298,42 206,42 216,22" fill="var(--step-3)"/>
      <polygon points="206,2 298,2 310,22 298,42 206,42 216,22" fill="url(#gloss)"/>
      <text x="260" y="27">2011</text>
      <polygon points="309,2 401,2 413,22 401,42 309,42 319,22" fill="var(--step-4)"/>
      <polygon points="309,2 401,2 413,22 401,42 309,42 319,22" fill="url(#gloss)"/>
      <text x="363" y="27">2012</text>
      <polygon points="412,2 504,2 516,22 504,42 412,42 422,22" fill="var(--step-5)"/>
      <polygon points="412,2 504,2 516,22 504,42 412,42 422,22" fill="url(#gloss)"/>
      <text x="466" y="27">2013</text>
    </g>
  </svg>
  <div class="timeline-notes">
    <p class="timeline-note">Lorem ipsum dolor sit amet, semper mauris fermentum fusce optio, neque eget, quam in dui</p>
    <p class="timeline-note">Lorem ipsum dolor sit amet, semper mauris fermentum fusce optio, neque eget, quam in dui</p>
    <p class="timeline-note">Lorem ipsum dolor sit amet, semper mauris fermentum fusce optio, neque eget, quam in dui</p>
    <p class="timeline-note">Lorem ipsum dolor sit amet, semper mauris fermentum fusce optio, neque eget, quam in dui</p>
    <p class="timeline-note">Lorem ipsum dolor sit amet, semper mauris fermentum fusce optio, neque eget, quam in dui</p>
  </div>
  <svg class="footer-wave" viewBox="0 0 553 80" aria-hidden="true">
    <path d="M0 2 C40 40 140 52 260 44 C380 36 470 22 553 24 L553 80 L0 80 Z" fill="url(#waveFill1)"/>
    <path d="M0 2 C40 40 140 52 260 44 C380 36 470 22 553 24" fill="none" stroke="#c8c8c8" stroke-width="1.5"/>
    <path d="M70 60 C200 66 380 42 553 40" fill="none" stroke="#bdbdbd" stroke-width="3"/>
  </svg>
  <div class="footer-badge">KO</div>
</section>

<section class="slide slide--rationale">
  <div class="header-bar">KO Mall</div>
  <div class="section-tag">Exetutive Summary</div>
  <h1 class="slide-title" style="top:34px;left:-5px;">Rational</h1>
  <ul class="pillar-list">
    <li class="pillar"><div class="pillar-track"></div><div class="pillar-label">Foulset<br>Retail</div></li>
    <li class="pillar"><div class="pillar-track"></div><div class="pillar-label">Local<br>Fows</div></li>
    <li class="pillar"><div class="pillar-track"></div><div class="pillar-label">Retail<br>Foul</div></li>
    <li class="pillar"><div class="pillar-track"></div><div class="pillar-label">Develop<br>Theaters</div></li>
    <li class="pillar"><div class="pillar-track"></div><div class="pillar-label">Hyper<br>Market</div></li>
  </ul>
  <svg class="footer-wave" viewBox="0 0 553 80" aria-hidden="true">
    <path d="M0 2 C40 40 140 52 260 44 C380 36 470 22 553 24 L553 80 L0 80 Z" fill="url(#waveFill1)"/>
    <path d="M0 2 C40 40 140 52 260 44 C380 36 470 22 553 24" fill="none" stroke="#c8c8c8" stroke-width="1.5"/>
    <path d="M70 60 C200 66 380 42 553 40" fill="none" stroke="#bdbdbd" stroke-width="3"/>
  </svg>
  <div class="footer-badge">KO</div>
</section>

<section class="slide slide--chart">
  <div class="header-bar">KO Mall</div>
  <svg class="bar-chart" viewBox="0 0 553 330">
    <g stroke="#d0d0d0" stroke-width="1">
      <line x1="66" y1="98" x2="449" y2="98"/>
      <line x1="66" y1="132" x2="449" y2="132"/>
      <line x1="66" y1="165" x2="449" y2="165"/>
      <line x1="66" y1="199" x2="449" y2="199"/>
      <line x1="66" y1="233" x2="449" y2="233"/>
      <line x1="66" y1="266" x2="449" y2="266"/>
    </g>
    <line x1="66" y1="300" x2="449" y2="300" stroke="#888"/>
    <line x1="66" y1="98" x2="66" y2="300" stroke="#888"/>
    <g font-size="12" fill="#1a1a1a" text-anchor="end">
      <text x="56" y="104">6</text><text x="56" y="138">5</text><text x="56" y="171">4</text>
      <text x="56" y="205">3</text><text x="56" y="239">2</text><text x="56" y="272">1</text>
      <text x="56" y="306">0</text>
    </g>
    <rect x="84" y="155" width="21" height="145" fill="var(--grey-dark)"/>
    <rect x="105" y="219" width="21" height="81" fill="var(--grey-light)"/>
    <rect x="126" y="233" width="21" height="67" fill="var(--grey-mid)"/>
    <rect x="180" y="216" width="21" height="84" fill="var(--grey-dark)"/>
    <rect x="201" y="152" width="21" height="148" fill="var(--grey-light)"/>
    <rect x="222" y="233" width="21" height="67" fill="var(--grey-mid)"/>
    <rect x="276" y="182" width="21" height="118" fill="var(--grey-dark)"/>
    <rect x="297" y="239" width="21" height="61" fill="var(--grey-light)"/>
    <rect x="318" y="199" width="21" height="101" fill="var(--grey-mid)"/>
    <rect x="372" y="148" width="21" height="152" fill="var(--grey-dark)"/>
    <rect x="393" y="206" width="21" height="94" fill="var(--grey-light)"/>
    <rect x="414" y="132" width="21" height="168" fill="var(--grey-mid)"/>
    <g font-size="12" fill="#1a1a1a" text-anchor="middle">
      <text x="114" y="320">Category 1</text><text x="210" y="320">Category 2</text>
      <text x="306" y="320">Category 3</text><text x="402" y="320">Category 4</text>
    </g>
    <g font-size="12" fill="#1a1a1a">
      <rect x="465" y="181" width="8" height="8" fill="var(--grey-dark)"/><text x="479" y="189">Series 1</text>
      <rect x="465" y="202" width="8" height="8" fill="var(--grey-light)"/><text x="479" y="210">Series 2</text>
      <rect x="465" y="223" width="8" height="8" fill="var(--grey-mid)"/><text x="479" y="231">Series 3</text>
    </g>
  </svg>
  <svg class="footer-wave" viewBox="0 0 553 80" aria-hidden="true">
    <path d="M0 2 C40 40 140 52 260 44 C380 36 470 22 553 24 L553 80 L0 80 Z" fill="url(#waveFill1)"/>
    <path d="M0 2 C40 40 140 52 260 44 C380 36 470 22 553 24" fill="none" stroke="#c8c8c8" stroke-width="1.5"/>
    <path d="M70 60 C200 66 380 42 553 40" fill="none" stroke="#bdbdbd" stroke-width="3"/>
  </svg>
  <div class="footer-badge">KO</div>
</section>

</body>
</html>
```